Premium modern eliquids labels 84.5 x 80 mm

I am looking for modern graphics for the labels of a new eliquid line that will have 4 different types of eliquids. It will have a tobacco one (brown colours maybe), a fruity one (bright colours maybe), a minty one (green colours maybe) and a creamy one (beige colours maybe).
I will need one of them to see how the design is, that design will have to be adapted to the other 3 colours of the label.
The brand logo is attached. I also attached a sample of what is mandatory to write on the label, you can change size, place and font of what is written, the only thing that cannot be reduced is the yellow parts. I attach the bottle that we will use.The size of the label is 84.5 x 80 mm (base x height).

Target Market(s)

vapers

Requirements
Must have
• My project must have one of the labels.

```html
<!DOCTYPE html>
<html lang="it">
<head>
<meta charset="utf-8">
<title>Nimbus Drops – eLiquid label range</title>
<link rel="stylesheet" href="https://fonts.googleapis.com/css2?family=Archivo:wght@300;400;800&family=Archivo+Narrow:wght@600&display=swap">
<style>
  :root {
    --canvas: #dcdcdc;
    --white: #ffffff;
    --menta-body: #1f9a48;  --menta-band: #8cc63f;  --menta-sub: #e4f2c4;  --menta-base: #149244;
    --mango-body: #e8892a;  --mango-band: #111111;  --mango-sub: #f08a24;  --mango-base: #e8892a;
    --tabacco-body: #5e4636; --tabacco-band: #c98b52; --tabacco-sub: #f3dcc0; --tabacco-base: #5e4636;
    --crema-body: #efe2bd;  --crema-band: #2c4660;  --crema-sub: #d8d2bd;  --crema-base: #efe2bd; --crema-ink: #2c4660;
    --mirtillo-body: #3b2a78; --mirtillo-band: #f0952a; --mirtillo-sub: #fbe0bd; --mirtillo-base: #3b2a78;
    --ciliegia-body: #8e1a1e; --ciliegia-band: #2a9a48; --ciliegia-sub: #c8ecd2; --ciliegia-base: #8e1a1e;
    --uva-body: #4a2266;    --uva-band: #8cc63f;    --uva-sub: #eaf5d4;    --uva-base: #4a2266;
    --fragola-body: #d4262a; --fragola-band: #7a1418; --fragola-sub: #f4c4c4; --fragola-base: #d4262a;
    --anguria-body: #1f9a48; --anguria-band: #d8243a; --anguria-sub: #f8d0d6; --anguria-base: #169a52;
  }
  * { box-sizing: border-box; margin: 0; padding: 0; }
  html, body { width: 1200px; height: 675px; overflow: hidden; }
  body {
    background: var(--canvas);
    font-family: "Archivo", Arial, sans-serif;
    display: flex; align-items: center; justify-content: center;
  }
  .range { display: flex; gap: 8px; }
  .label {
    width: 120px; height: 440px;
    display: flex; flex-direction: column;
    color: var(--white);
    overflow: hidden;
  }
  .label__body {
    flex: 1; background: var(--body);
    display: flex; align-items: center; justify-content: center;
  }
  .label__brand {
    writing-mode: vertical-rl; transform: rotate(180deg);
    font-weight: 800; font-size: 34px; letter-spacing: 1px; line-height: 1;
    white-space: nowrap; color: var(--ink, var(--white));
  }
  .label__flavour {
    height: 58px; background: var(--band);
    display: flex; flex-direction: column; align-items: center; justify-content: center; gap: 6px;
    padding: 0 4px;
  }
  .label__name {
    font-family: "Archivo Narrow", "Arial Narrow", sans-serif;
    font-weight: 600; font-size: 11.5px; line-height: 1;
    white-space: nowrap; max-width: 100%;
  }
  .label__nicotine {
    font-weight: 300; font-size: 7px; letter-spacing: 1.6px; line-height: 1;
    color: var(--sub); white-space: nowrap;
  }
  .label__volume {
    height: 44px; background: var(--base);
    display: flex; align-items: center; justify-content: space-between;
    padding: 0 14px; font-weight: 300; font-size: 11px; color: var(--ink, var(--white));
  }
  .menta    { --body: var(--menta-body);    --band: var(--menta-band);    --sub: var(--menta-sub);    --base: var(--menta-base); }
  .mango    { --body: var(--mango-body);    --band: var(--mango-band);    --sub: var(--mango-sub);    --base: var(--mango-base); }
  .tabacco  { --body: var(--tabacco-body);  --band: var(--tabacco-band);  --sub: var(--tabacco-sub);  --base: var(--tabacco-base); }
  .crema    { --body: var(--crema-body);    --band: var(--crema-band);    --sub: var(--crema-sub);    --base: var(--crema-base); }
  .crema .label__body, .crema .label__volume { --ink: var(--crema-ink); }
  .mirtillo { --body: var(--mirtillo-body); --band: var(--mirtillo-band); --sub: var(--mirtillo-sub); --base: var(--mirtillo-base); }
  .ciliegia { --body: var(--ciliegia-body); --band: var(--ciliegia-band); --sub: var(--ciliegia-sub); --base: var(--ciliegia-base); }
  .uva      { --body: var(--uva-body);      --band: var(--uva-band);      --sub: var(--uva-sub);      --base: var(--uva-base); }
  .fragola  { --body: var(--fragola-body);  --band: var(--fragola-band);  --sub: var(--fragola-sub);  --base: var(--fragola-base); }
  .anguria  { --body: var(--anguria-body);  --band: var(--anguria-band);  --sub: var(--anguria-sub);  --base: var(--anguria-base); }
</style>
</head>
<body>
  <main class="range">
    <article class="label menta">
      <div class="label__body"><span class="label__brand">NIMBUS DROPS</span></div>
      <div class="label__flavour"><span class="label__name">MENTA GHIACCIATA</span><span class="label__nicotine">SENZA NICOTINA</span></div>
      <div class="label__volume"><span>20ml</span><span>eLiquid</span></div>
    </article>
    <article class="label mango">
      <div class="label__body"><span class="label__brand">NIMBUS DROPS</span></div>
      <div class="label__flavour"><span class="label__name">MANGO TROPICALE</span><span class="label__nicotine">SENZA NICOTINA</span></div>
      <div class="label__volume"><span>20ml</span><span>eLiquid</span></div>
    </article>
    <article class="label tabacco">
      <div class="label__body"><span class="label__brand">NIMBUS DROPS</span></div>
      <div class="label__flavour"><span class="label__name">MISCELA IL TABACCO</span><span class="label__nicotine">SENZA NICOTINA</span></div>
      <div class="label__volume"><span>20ml</span><span>eLiquid</span></div>
    </article>
    <article class="label crema">
      <div class="label__body"><span class="label__brand">NIMBUS DROPS</span></div>
      <div class="label__flavour"><span class="label__name">CREMA D'ASSO</span><span class="label__nicotine">SENZA NICOTINA</span></div>
      <div class="label__volume"><span>20ml</span><span>eLiquid</span></div>
    </article>
    <article class="label mirtillo">
      <div class="label__body"><span class="label__brand">NIMBUS DROPS</span></div>
      <div class="label__flavour"><span class="label__name">MIRTILLO</span><span class="label__nicotine">SENZA NICOTINA</span></div>
      <div class="label__volume"><span>20ml</span><span>eLiquid</span></div>
    </article>
    <article class="label ciliegia">
      <div class="label__body"><span class="label__brand">NIMBUS DROPS</span></div>
      <div class="label__flavour"><span class="label__name">CILIEGIA</span><span class="label__nicotine">SENZA NICOTINA</span></div>
      <div class="label__volume"><span>20ml</span><span>eLiquid</span></div>
    </article>
    <article class="label uva">
      <div class="label__body"><span class="label__brand">NIMBUS DROPS</span></div>
      <div class="label__flavour"><span class="label__name">UVA</span><span class="label__nicotine">SENZA NICOTINA</span></div>
      <div class="label__volume"><span>20ml</span><span>eLiquid</span></div>
    </article>
    <article class="label fragola">
      <div class="label__body"><span class="label__brand">NIMBUS DROPS</span></div>
      <div class="label__flavour"><span class="label__name">FRAGOLA</span><span class="label__nicotine">SENZA NICOTINA</span></div>
      <div class="label__volume"><span>20ml</span><span>eLiquid</span></div>
    </article>
    <article class="label anguria">
      <div class="label__body"><span class="label__brand">NIMBUS DROPS</span></div>
      <div class="label__flavour"><span class="label__name">ANGURIA</span><span class="label__nicotine">SENZA NICOTINA</span></div>
      <div class="label__volume"><span>20ml</span><span>eLiquid</span></div>
    </article>
  </main>
</body>
</html>
```